Packaging/hanging backer for Lunfrew™ No-Pull Dog Harness

Product measures 1.25” x 13” (33cm x 3.8cm)

Looking for hang packaging for dog harness. Possibly a backer board. Need extra room on packaging for instructions/customer education as this product is not self-explanatory. Would like packaging art to fit with my brand/website. Examples are given in attached files and the website is: www.lunfrewshop.com.

The goal is to be bright and eye catching, while inducing some trust. Backer board is suggested, but not required. Would also be interested in a clear plastic box, or paper tube. Would like to not be overly wasteful with packaging.

Target Market(s)

Dog Owners.

Industry/Entity Type

Pet Products: Harnesses/collars/leashes

Font styles to use
Sans Serif

Requirements
Must have
• Room for easy customer education on the front of the package. Must be able to be hung in the store.
Nice to have
• I would like to be able to create packaging for other lines of harnesses by just changing the colors. Would like a similar feel to design of website www.lunfrewshop.com. Smaller/less packaging would better and it’s ok if the harness hangs off the bottom if creating a backer.

```html
<!DOCTYPE html>
<html lang="en">
<head>
<meta charset="utf-8">
<title>Lunfrew™ No-Pull Dog Harness – Hanging Backer</title>
<link rel="stylesheet" href="https://fonts.googleapis.com/css2?family=Roboto+Condensed:wght@300;400;500;700&display=swap">
<style>
  :root{
    --ink:#111111;
    --navy:#2a1f7c;
    --badge-red:#e3001b;
    --white:#ffffff;
    --warm-left:#e84a4c;
    --pink-mid:#f2a9bf;
    --lilac:#c9a9d6;
    --blue-right:#3f78c6;
    --harness-green:#4fc25a;
    --harness-dark:#2f8f3a;
  }
  html,body{margin:0;padding:0;overflow:hidden;background:var(--white);}
  .canvas{position:relative;width:1200px;height:2538px;overflow:hidden;background:var(--white);}
  .backer{
    position:absolute;left:22px;top:4px;width:1172px;height:2528px;
    border:3px solid var(--ink);border-radius:80px;box-sizing:border-box;overflow:hidden;
    background:
      linear-gradient(160deg, rgba(255,255,255,.35) 0%, rgba(255,255,255,0) 30%),
      linear-gradient(100deg, var(--warm-left) 0%, #ef7e95 25%, var(--pink-mid) 45%, var(--lilac) 65%, #7f9fd8 82%, var(--blue-right) 100%);
    font-family:"Roboto Condensed", sans-serif;
  }
  .hang-hole{position:absolute;left:362px;top:14px;width:490px;height:140px;}
  .size-badge{
    position:absolute;left:75px;top:64px;width:156px;height:156px;border-radius:50%;
    background:var(--badge-red);color:var(--white);
    display:flex;align-items:center;justify-content:center;
    font-weight:700;font-size:64px;letter-spacing:1px;
  }
  .brand-name{
    position:absolute;right:40px;top:150px;color:var(--white);
    font-weight:700;font-size:60px;line-height:1;
  }
  .illustration{
    position:absolute;left:258px;top:1400px;width:914px;height:1128px;
    background:linear-gradient(170deg,#b77a55 0%,#d85c6f 35%,#8b5fb0 65%,#f0a43a 100%);
    border-radius:40px 40px 0 0;opacity:.9;
  }
  .product-photo{
    position:absolute;left:40px;top:262px;width:272px;height:2220px;
    background:linear-gradient(180deg,#cfd3d6 0%,var(--harness-green) 8%,var(--harness-green) 60%,var(--harness-dark) 100%);
    border-radius:40px;
  }
  .copy{position:absolute;left:505px;top:284px;width:620px;color:var(--ink);white-space:nowrap;}
  .title{
    margin:0;color:var(--navy);font-weight:700;font-size:136px;line-height:133px;letter-spacing:-1px;
    transform:scaleX(.87);transform-origin:left top;
  }
  .intro{margin:10px 0 0;font-weight:300;font-size:37px;line-height:48px;}
  .feature{margin:30px 0 0 22px;}
  .feature h2{margin:0;font-weight:500;font-size:38px;line-height:44px;}
  .feature p{margin:4px 0 0;font-weight:300;font-size:30px;line-height:40.5px;}
</style>
</head>
<body>
<div class="canvas">
  <div class="backer">
    <svg class="hang-hole" viewBox="0 0 490 140" aria-hidden="true">
      <path d="M60 42 H184 A60 60 0 0 1 304 42 H430 A48 48 0 0 1 430 138 H60 A48 48 0 0 1 60 42 Z"
            fill="#ffffff" stroke="#111111" stroke-width="4"/>
    </svg>

    <div class="size-badge">M-L</div>
    <div class="brand-name">Lunfrew™</div>

    <div class="illustration" role="img" aria-label="Pop-art illustration of a colourful geometric dog in front of a brick wall with a red LOVE burst, hearts and paint splashes"></div>
    <div class="product-photo" role="img" aria-label="Product photo of the green nylon no-pull harness with metal D-ring, black buckle and leash clip"></div>

    <div class="copy">
      <h1 class="title">No-Pull<br>Pet Harness</h1>
      <p class="intro">This medium-large no-pull harness fits most<br>dogs 40 to 120 pounds (18kg - 55kg).</p>

      <section class="feature">
        <h2>Freedom of Movement</h2>
        <p>Our no-pull dog harness placement keeps the<br>leash from getting wrapped up or trapped in their<br>legs. That way, they can explore without constantly<br>getting tangled up, and you don't have to<br>constantly be untangling, or pulling the leash back<br>out from under them.</p>
      </section>

      <section class="feature">
        <h2>Professional Grade Construction</h2>
        <p>We use bar-tack stitching, which is stronger than<br>the more common "box-x" found in other pet<br>products.<br>This is the type of stitching you will find in rock<br>climbing accessories because of its strength and<br>durability. If it is good enough for those hiking up<br>Everest, it is good enough for your furry friend!</p>
      </section>
    </div>
  </div>
</div>
</body>
</html>
```